KTV Consulting

Government/Entitlement Consulting Services- I assist developers obtain entitlements from local, state and federal government agencies so that they can build their projects. Often these projects are very complicated and political and may face community opposition.

Target Market(s)

Real Estate Developers

Industry/Entity Type

Business Consultant

Contact Information for Business Card

Dana Pelletier
Principal

Font styles to use
Serif
Sans Serif

Requirements
Must have
• Classy and professional appeal.
Nice to have
• I like a combination of a mat and glossy finish. I've seen that done with black and then a bold color for a pop, but am not 100% committed to that.

```html
<!DOCTYPE html>
<html lang="en">
<head>
<meta charset="utf-8">
<title>KTV Consulting – Business Card</title>
<link rel="stylesheet" href="https://fonts.googleapis.com/css2?family=Arimo:wght@400;700&display=swap">
<style>
  :root {
    --backdrop: #e9e7e3;
    --card: #fbfbfa;
    --ink: #151515;
    --ink-soft: #2a2a2a;
    --band: #060606;
    --band-sheen: #2c2c2c;
    --band-text: #ffffff;
    --rule: #3a3a3a;
  }
  * { box-sizing: border-box; margin: 0; padding: 0; }
  html, body {
    width: 1200px; height: 892px; overflow: hidden;
    background: var(--backdrop);
    font-family: "Arimo", Arial, sans-serif;
    color: var(--ink);
  }
  .stage {
    width: 1200px; height: 892px;
    display: flex; flex-direction: column; align-items: center; justify-content: center;
    gap: 40px;
  }
  .card {
    position: relative;
    width: 700px; height: 400px;
    background: var(--card);
    box-shadow: 0 6px 18px rgba(0,0,0,0.18);
    overflow: hidden;
  }
  /* Front */
  .front__company {
    position: absolute; left: 58px; top: 74px;
    font-size: 40px; font-weight: 700; letter-spacing: -0.5px;
  }
  .front__divider {
    position: absolute; left: 400px; top: 40px;
    width: 1px; height: 215px; background: var(--rule);
  }
  .front__person {
    position: absolute; left: 430px; top: 70px;
  }
  .front__name { font-size: 20px; color: var(--ink-soft); }
  .front__title { font-size: 14px; font-style: italic; color: var(--ink-soft); margin-top: 3px; }
  .front__contacts {
    position: absolute; left: 430px; top: 178px;
    list-style: none;
  }
  .contact {
    display: flex; align-items: center; gap: 10px;
    font-size: 16px; color: var(--ink-soft);
    height: 24px;
  }
  .contact svg { width: 16px; height: 16px; flex: none; }
  .front__band {
    position: absolute; left: 0; bottom: 0;
    width: 100%; height: 92px;
    background: linear-gradient(180deg, var(--band-sheen) 0%, var(--band) 35%, var(--band) 100%);
    display: flex; align-items: center;
    padding-left: 110px;
  }
  .front__address {
    color: var(--band-text);
    font-size: 22px; letter-spacing: 0.3px;
  }
  /* Back */
  .back {
    display: flex; align-items: center; justify-content: center;
  }
  .back__company {
    font-size: 64px; font-weight: 700; letter-spacing: -1px;
  }
</style>
</head>
<body>
<main class="stage">
  <section class="card front" aria-label="Business card front">
    <h1 class="front__company">KTV Consulting</h1>
    <div class="front__divider"></div>
    <div class="front__person">
      <p class="front__name">Dana Pelletier</p>
      <p class="front__title">Principal</p>
    </div>
    <ul class="front__contacts">
      <li class="contact">
        <svg viewBox="0 0 16 16" aria-hidden="true">
          <rect width="16" height="16" rx="2" fill="#151515"/>
          <path d="M4.5 3.5h2l1 2.5-1.3 1a6 6 0 0 0 2.8 2.8l1-1.3 2.5 1v2a1 1 0 0 1-1 1A8.5 8.5 0 0 1 3.5 4.5a1 1 0 0 1 1-1z" fill="#fff"/>
        </svg>
        <span>555-214-0187</span>
      </li>
      <li class="contact">
        <svg viewBox="0 0 16 16" aria-hidden="true">
          <rect width="16" height="16" rx="2" fill="#151515"/>
          <circle cx="8" cy="8" r="4.6" fill="none" stroke="#fff" stroke-width="1.2"/>
          <ellipse cx="8" cy="8" rx="2" ry="4.6" fill="none" stroke="#fff" stroke-width="1"/>
          <path d="M3.4 8h9.2" stroke="#fff" stroke-width="1"/>
        </svg>
        <span>www.ktvadvisory.com</span>
      </li>
      <li class="contact">
        <svg viewBox="0 0 16 16" aria-hidden="true">
          <rect width="16" height="16" rx="2" fill="#151515"/>
          <rect x="3" y="4.5" width="10" height="7" fill="none" stroke="#fff" stroke-width="1.2"/>
          <path d="M3 4.8l5 3.8 5-3.8" fill="none" stroke="#fff" stroke-width="1.2"/>
        </svg>
        <span>hello@ktvadvisory.com</span>
      </li>
    </ul>
    <div class="front__band">
      <p class="front__address">14 Harlow Lane Westbury NSW 2150</p>
    </div>
  </section>

  <section class="card back" aria-label="Business card back">
    <p class="back__company">KTV Consulting</p>
  </section>
</main>
</body>
</html>
```